Business Card Design Project

I have a two letter domain name qo.com.au (lower case font please). I want a business card, cum logo that is die cut (around the qo segment at least) that fits standard business card size.
qo is all about what 'I am' - a journalist, blogger, analyst, commentator. My mantra is "I wander so qo'.
The reverse of the card only needs my name Lon Fitch, email lon@qo.com.au and mobile +61 400 555 817
Target Market(s)
Mainly people that will use my professional writing services and suppliers that will provide product for review
Industry/Entity Type
Business
Requirements
Must have
- One side is qo.com.au (hint - the .com.au can be vertical or horizontal to fit - the qo should be as large as possible).
The other requires large size font name, email and phone details (so no one needs glasses to read it).
The die cut can be just to highlight the qo segment - need not be around the whole card.
Font used in the past was Belwe (old style - very much like the i used in the information symbol).
Colours - no preference - prefer two colour to process colour but can also be an outline font instead of solid colour.

```html
<!DOCTYPE html>
<html lang="en">
<head>
<meta charset="utf-8">
<title>qo.com.au business card</title>
<link rel="stylesheet" href="https://fonts.googleapis.com/css2?family=Comfortaa:wght@700&family=Share+Tech+Mono&family=Zilla+Slab:wght@300&display=swap">
<style>
  :root {
    --backdrop: #4b4f56;
    --card-coral: #ec6a5c;
    --card-coral-light: #f06d5f;
    --card-coral-deep: #e2655a;
    --ink-white: #ffffff;
  }
  * { box-sizing: border-box; margin: 0; padding: 0; }
  html, body {
    width: 1200px;
    height: 1000px;
    overflow: hidden;
  }
  body {
    background: var(--backdrop);
    display: flex;
    flex-direction: column;
    align-items: center;
    justify-content: center;
    gap: 60px;
  }
  .card {
    width: 700px;
    height: 400px;
    background: linear-gradient(135deg, var(--card-coral-deep) 0%, var(--card-coral) 50%, var(--card-coral-light) 100%);
    color: var(--ink-white);
  }
  /* Front face */
  .card-front {
    display: flex;
    align-items: center;
    padding-left: 50px;
  }
  .front-row {
    display: flex;
    align-items: baseline;
    gap: 34px;
  }
  .brand {
    display: flex;
    align-items: center;
    gap: 16px;
  }
  .brand-dot {
    width: 40px;
    height: 40px;
    border-radius: 50%;
    background: var(--ink-white);
    flex: none;
  }
  .brand-name {
    font-family: "Comfortaa", sans-serif;
    font-weight: 700;
    font-size: 56px;
    line-height: 1;
  }
  .tagline {
    font-family: "Share Tech Mono", monospace;
    font-size: 15px;
    letter-spacing: 4px;
    text-transform: uppercase;
    white-space: nowrap;
  }
  /* Back face */
  .card-back {
    padding: 62px 0 0 80px;
  }
  .holder-name {
    font-family: "Comfortaa", sans-serif;
    font-weight: 700;
    font-size: 46px;
    margin-bottom: 34px;
  }
  .contact-line {
    font-family: "Zilla Slab", serif;
    font-weight: 300;
    font-size: 40px;
    line-height: 1.5;
  }
</style>
</head>
<body>
  <section class="card card-front" aria-label="Card front">
    <div class="front-row">
      <div class="brand">
        <span class="brand-dot"></span>
        <span class="brand-name">qo.com.au</span>
      </div>
      <p class="tagline">"I wander so qo'</p>
    </div>
  </section>

  <section class="card card-back" aria-label="Card back">
    <h1 class="holder-name">Lon Fitch</h1>
    <p class="contact-line">email lon@qo.com.au</p>
    <p class="contact-line">mobile +61 400 555 817</p>
  </section>
</body>
</html>
```